Business Card Design Project

Hello! We need a business card design for a new company opening up in Downtown Dallas called Marbrook Cupcakes. We are a cupcake factory and our primary colors are Harbor Teal and Brown. We want to have a design that can be used for multiple positions (Owner/Operations Manager, Assistant Operations Manager, Decorator, Baker, Corporate Sale Rep, Special Events Rep etc) We would like for it to be double sided. Use the following information in your designs:

Renata Vasquill
Assistant Operations Manager
renata@marbrookcupcakes.example
T555.318.9047

Store Hours:
Mon-Thur 10am-9pm
Fri-Sat 10am-10pm
Sun 12pm-7pm

website: www.marbrookcupcakes.example

Address: 2735 Quarry Ln, Dallas TX 75999

The logo is attached.

Industry/Entity Type

Business

Requirements
Must have
• It must be Harbor Teal and Brown.
Nice to have
• Nice for it to be double sided.
Should not have
• No graphics like a cupcake. Just the word logo.

```html
<!DOCTYPE html>
<html lang="en">
<head>
<meta charset="utf-8">
<title>Marbrook Cupcakes – Business Cards</title>
<link href="https://fonts.googleapis.com/css2?family=Arimo:wght@400;700&family=Raleway:wght@300&display=swap" rel="stylesheet">
<style>
  :root {
    --harbor-teal: #69c5cd;
    --cocoa: #3c1b10;
    --ink: #000000;
    --paper: #ffffff;
    --stage: #e9e4df;
    --text-dark: #3a1f16;
  }
  * { margin: 0; padding: 0; box-sizing: border-box; }
  html, body { width: 1200px; height: 715px; overflow: hidden; }
  body {
    background: var(--stage);
    position: relative;
    font-family: "Arimo", Arial, sans-serif;
  }
  .card {
    position: absolute;
    width: 525px;
    height: 300px;
    border-radius: 18px;
    overflow: hidden;
  }
  .card--front { left: 53px; top: 31px; background: var(--ink); border: 1px solid #222; }
  .card--white { left: 622px; top: 39px; background: var(--paper); border: 1px solid #555; }
  .card--teal  { left: 50px;  top: 376px; height: 298px; background: var(--harbor-teal); border: 1px solid #333; }
  .card--cocoa { left: 628px; top: 370px; height: 298px; background: var(--cocoa); border: 1px solid #1a0a05; }

  .wordmark {
    position: absolute;
    font-family: "Raleway", "Arimo", sans-serif;
    font-weight: 300;
    font-size: 50px;
    line-height: 1.02;
    text-align: right;
    letter-spacing: 0.5px;
  }
  .card--front .wordmark { right: 88px; top: 34px; color: var(--harbor-teal); }
  .card--white .wordmark { right: 38px; top: 56px; color: var(--text-dark); font-size: 58px; }
  .card--teal  .wordmark { right: 40px; top: 48px; color: var(--paper); font-size: 58px; }
  .card--cocoa .wordmark { right: 40px; top: 48px; color: var(--paper); font-size: 58px; }

  .contact-band {
    position: absolute;
    left: 0; right: 0;
    top: 170px;
    height: 87px;
    background: var(--harbor-teal);
    border-bottom: 3px solid var(--paper);
    box-shadow: 0 -3px 0 var(--paper) inset;
  }
  .contact-band::after {
    content: "";
    position: absolute; left: 0; right: 0; bottom: -7px; height: 1px;
    background: var(--paper);
  }
  .address {
    position: absolute;
    right: 307px; top: 27px;
    text-align: right;
    font-size: 13.5px;
    line-height: 22px;
    letter-spacing: 0.6px;
    color: var(--text-dark);
  }
  .band-divider {
    position: absolute; left: 230px; top: 10px;
    width: 1px; height: 66px; background: var(--paper);
  }
  .contact-list {
    position: absolute; left: 242px; top: 10px;
    list-style: none;
    font-size: 13px;
    line-height: 23px;
    color: var(--text-dark);
  }
  .contact-list li { display: flex; align-items: center; gap: 6px; }
  .contact-list svg { width: 10px; height: 10px; fill: var(--text-dark); flex: none; }

  .person {
    position: absolute; left: 84px; top: 272px;
    font-size: 14px; color: var(--paper);
  }
  .person__name { color: var(--harbor-teal); font-weight: 700; font-size: 17px; letter-spacing: 0.3px; }

  .hours {
    position: absolute; left: 24px; top: 211px;
    font-size: 15.5px; line-height: 19px; letter-spacing: 0.9px;
  }
  .hours__title { font-weight: 700; }
  .card--white .hours { color: var(--text-dark); }
  .card--white .hours__title { color: var(--harbor-teal); }
  .card--teal .hours, .card--cocoa .hours { color: var(--paper); }

  .site {
    position: absolute; right: 38px; top: 244px;
    font-size: 13px; letter-spacing: 0.4px;
  }
  .card--white .site { color: var(--text-dark); }
  .site__accent { color: var(--harbor-teal); }
  .card--teal .site, .card--cocoa .site { color: var(--paper); top: 246px; right: 55px; }
</style>
</head>
<body>

  <section class="card card--front" aria-label="Card front">
    <div class="wordmark">Marbrook<br>Cupcakes</div>
    <div class="contact-band">
      <p class="address">2735 Quarry Ln<br>Dallas TX 75999</p>
      <span class="band-divider"></span>
      <ul class="contact-list">
        <li><svg viewBox="0 0 10 10"><path d="M2 0.5 3.6 2.6 2.7 3.7a6 6 0 0 0 3.6 3.6l1.1-.9 2.1 1.6-.9 1.5C4.3 9.6.4 5.7.5 1.4Z"/></svg>555.318.9047</li>
        <li><svg viewBox="0 0 10 10"><path d="M0 2h10v6H0Z" opacity=".9"/><path d="M0 2l5 3.4L10 2" fill="none" stroke="#69c5cd" stroke-width="1"/></svg>renata@marbrookcupcakes.example</li>
        <li><svg viewBox="0 0 10 10"><circle cx="5" cy="5" r="4.5"/><path d="M.5 5h9M5 .5c2.5 2.5 2.5 6.5 0 9M5 .5c-2.5 2.5-2.5 6.5 0 9" fill="none" stroke="#69c5cd" stroke-width=".8"/></svg>www.marbrookcupcakes.example</li>
      </ul>
    </div>
    <p class="person"><span class="person__name">Renata Vasquill,</span> Assistant Operations Manager</p>
  </section>

  <section class="card card--white" aria-label="Card back, white">
    <div class="wordmark">Marbrook<br>Cupcakes</div>
    <div class="hours">
      <p class="hours__title">Store Hours</p>
      <p>Mon-Thur 10am-9pm</p>
      <p>Fri-Sat 10am-10pm</p>
      <p>Sun 12pm-7pm</p>
    </div>
    <p class="site">www.<span class="site__accent">marbrookcupcakes</span>.example</p>
  </section>

  <section class="card card--teal" aria-label="Card back, teal">
    <div class="wordmark">Marbrook<br>Cupcakes</div>
    <div class="hours">
      <p class="hours__title">Store Hours</p>
      <p>Mon-Thur 10am-9pm</p>
      <p>Fri-Sat 10am-10pm</p>
      <p>Sun 12pm-7pm</p>
    </div>
    <p class="site">www.marbrookcupcakes.example</p>
  </section>

  <section class="card card--cocoa" aria-label="Card back, brown">
    <div class="wordmark">Marbrook<br>Cupcakes</div>
    <div class="hours">
      <p class="hours__title">Store Hours</p>
      <p>Mon-Thur 10am-9pm</p>
      <p>Fri-Sat 10am-10pm</p>
      <p>Sun 12pm-7pm</p>
    </div>
    <p class="site">www.marbrookcupcakes.example</p>
  </section>

</body>
</html>
```